Certified Public Accountant specializing in tax preparation.

I need a business card designed that conveys knowledgeability, trustworthiness and competency. I am a licensed CPA and hold a Master's in taxation. As this is a personal service business, I would like to include my picture on the card.

```html
<!DOCTYPE html>
<html lang="en">
<head>
<meta charset="utf-8">
<title>Laura Pierce, CPA — Business Card</title>
<link href="https://fonts.googleapis.com/css2?family=Open+Sans:wght@400;600;700&display=swap" rel="stylesheet">
<style>
  :root {
    --backdrop: #c9cec6;
    --card: #f8f8f7;
    --charcoal: #393937;
    --salmon: #d58c6e;
    --ink: #2a2a2a;
    --white: #ffffff;
  }
  * { margin: 0; padding: 0; box-sizing: border-box; }
  html, body {
    width: 1200px; height: 900px; overflow: hidden;
    background: var(--backdrop);
    font-family: "Open Sans", Arial, sans-serif;
  }
  .card {
    position: absolute; left: 100px; top: 165px;
    width: 1000px; height: 570px;
    background: var(--card);
    box-shadow: 0 10px 30px rgba(0,0,0,0.18);
    overflow: hidden;
  }
  .band { position: absolute; height: 38px; }
  .band--top-dark { top: 0; left: 0; width: 52%; background: var(--charcoal); }
  .band--top-accent { top: 0; left: 52%; right: 0; background: var(--salmon); }
  .band--bottom-accent { bottom: 0; left: 0; width: 50%; background: var(--salmon); }
  .band--bottom-dark { bottom: 0; left: 50%; right: 0; background: var(--charcoal); }

  .portrait {
    position: absolute; left: 300px; top: 120px;
    width: 232px; height: 335px;
    background: linear-gradient(160deg, #b3673f 0%, #7a4a35 35%, #5b3a2e 60%, #d9b2bf 100%);
  }

  .identity { position: absolute; left: 560px; top: 118px; width: 340px; }
  .name {
    font-size: 25px; font-weight: 400; color: var(--ink);
    letter-spacing: 0.5px; line-height: 1;
  }
  .name strong { font-weight: 700; }
  .name .credential { font-size: 20px; }
  .services {
    margin-top: 4px; background: var(--charcoal); color: var(--white);
    font-size: 13px; font-weight: 600; letter-spacing: 1px;
    text-align: right; padding: 4px 12px 4px 0; width: 330px;
  }

  .contact {
    position: absolute; left: 575px; top: 200px;
    border-left: 3px solid var(--salmon);
    height: 250px; padding-left: 26px;
    color: var(--ink);
  }
  .phone { font-size: 22px; letter-spacing: 3px; line-height: 30px; }
  .email { font-size: 22px; letter-spacing: 2px; margin-top: 22px; }
  .address { font-size: 22px; line-height: 32px; margin-top: 28px; }
</style>
</head>
<body>
  <div class="card">
    <div class="band band--top-dark"></div>
    <div class="band band--top-accent"></div>
    <div class="band band--bottom-accent"></div>
    <div class="band band--bottom-dark"></div>

    <div class="portrait" role="img" aria-label="Portrait photo of the accountant in a pink blazer"></div>

    <div class="identity">
      <p class="name">LAURA <strong>PIERCE</strong> <span class="credential">,CPA</span></p>
      <p class="services">ACCOUNTING | TAX | CONSULTING</p>
    </div>

    <div class="contact">
      <p class="phone">555 . 214. 3098</p>
      <p class="phone">555 . 214. 3098</p>
      <p class="email">HELLO@PIERCECPA.COM</p>
      <p class="address">1487 Alder Grove Lane<br>Riverton</p>
    </div>
  </div>
</body>
</html>
```